Fern Guildworks Business Cards

Looking or a business card design for my start-up, called "Fern Guildworks".
Our tagline is "Unleashing the human potential for good through leadership, culture, and education."
Our mission-driven work includes professional/personal development workshops, educational design services, organizational & project management consulting, and coaching services for K-12 schools, organizations, and individuals.
You can check out the website we're building at fernguildworks.com
I select projects from designers who are highly responsive to feedback, engage in dialog about revisions, and provide all root/source documents (so please state in your initial submission that you agree to do so).
Looking forward to seeing your great designs!!
Updates
Hello everyone,
Industry/Entity Type
Building
Requirements
Must have
- Looking for a two sided design that includes our logo (I am uploading two variations that I would like incorporated in .ai format) and website on both sides.
The front side must include:
Logo, Name, Title, Phone, Email, Twitter handle
The back side must include: Logo, @ferngild (our organizational twitter handle)
Nice to have
- I like the rounded corner business cards, but that is not absolutely essential.
Should not have
- Colors beyond those presented in our logo.

```html
<!DOCTYPE html>
<html lang="en">
<head>
<meta charset="utf-8">
<title>Fern Guildworks Business Cards</title>
<link rel="stylesheet" href="https://fonts.googleapis.com/css2?family=Cormorant+Garamond:wght@500&family=Open+Sans:wght@600;700&display=swap">
<style>
  :root {
    --page: #e6e6e6;
    --card: #000000;
    --sky: #6fcde2;
    --stone: #bdb6ac;
    --text-light: #d8d8d8;
    --text-muted: #9a9a9a;
    --rule-dark: #1b1b1b;
    --white: #ffffff;
    --grey-band: #8a8a8a;
  }
  * { margin: 0; padding: 0; box-sizing: border-box; }
  html, body { width: 1200px; height: 911px; overflow: hidden; }
  body { background: var(--page); position: relative; font-family: "Open Sans", Arial, sans-serif; }

  .card {
    position: absolute; top: 300px; width: 544px; height: 308px;
    background: var(--card); border-radius: 14px; overflow: hidden;
    box-shadow: 0 6px 14px rgba(0,0,0,.35);
  }
  .card--front { left: 30px; }
  .card--back { left: 618px; }

  .brand-name, .tagline, .website { position: absolute; left: 0; right: 0; text-align: center; }
  .brand-name { font-family: "Open Sans", Arial, sans-serif; font-weight: 600; color: var(--stone); }
  .tagline { font-family: "Cormorant Garamond", Georgia, serif; font-weight: 500; color: var(--text-muted); text-transform: uppercase; }
  .website { font-family: "Cormorant Garamond", Georgia, serif; font-weight: 500; color: var(--text-muted); }

  .card--front .brand-name { top: 78px; font-size: 26px; }
  .card--front .tagline { top: 138px; font-size: 10px; letter-spacing: 3px; }
  .card--front .website { top: 154px; font-size: 9px; }

  .card--back .brand-name { top: 100px; font-size: 36px; }
  .card--back .tagline { top: 176px; font-size: 12px; letter-spacing: 4.5px; }
  .card--back .website { top: 198px; font-size: 11px; }

  .contact-row { position: absolute; left: 146px; right: 142px; height: 24px; display: flex; align-items: center; }
  .contact-row .icon { width: 22px; height: 22px; flex: none; }
  .contact-row .rule { flex: 1; height: 4px; margin: 0 6px 0 12px; border-radius: 2px; background: linear-gradient(90deg, var(--rule-dark), var(--sky)); }
  .contact-row .value { font-weight: 700; font-size: 14px; color: var(--text-light); white-space: nowrap; }
  .row--phone { top: 184px; }
  .row--email { top: 218px; }
  .row--social { top: 253px; }

  .social-dot { width: 16px; height: 16px; border-radius: 50%; background: var(--sky); flex: none; margin: 3px; }

  .back-handle { position: absolute; top: 232px; left: 0; right: 0; display: flex; justify-content: center; align-items: center; gap: 8px; }
  .back-handle .value { font-weight: 700; font-size: 14px; color: var(--text-light); }

  .stripes { position: absolute; left: 0; right: 0; top: 272px; }
  .stripes span { display: block; }
  .stripe--white { height: 4px; background: var(--white); margin-bottom: 2px; }
  .stripe--band { height: 10px; background: linear-gradient(90deg, var(--grey-band), var(--sky) 45%, var(--sky)); }
</style>
</head>
<body>
  <section class="card card--front" aria-label="Card front">
    <div class="brand-name">Fern Guildworks</div>
    <div class="tagline">Mentoring | Teams | Learning</div>
    <div class="website">www.fernguildworks.com</div>

    <div class="contact-row row--phone">
      <svg class="icon" viewBox="0 0 22 22" aria-label="Phone">
        <rect x="5" y="1.5" width="12" height="19" rx="2" fill="none" stroke="#6fcde2" stroke-width="1.6"/>
        <rect x="7" y="4" width="8" height="11" fill="#6fcde2" opacity=".5"/>
        <circle cx="11" cy="17.5" r="1.1" fill="#6fcde2"/>
      </svg>
      <span class="rule"></span>
      <span class="value">555 014 782</span>
    </div>

    <div class="contact-row row--email">
      <svg class="icon" viewBox="0 0 22 22" aria-label="Email">
        <rect x="1.5" y="4.5" width="19" height="13" fill="none" stroke="#6fcde2" stroke-width="1.6"/>
        <path d="M1.5 4.5 L11 12 L20.5 4.5 M1.5 17.5 L8.5 10.5 M20.5 17.5 L13.5 10.5" fill="none" stroke="#6fcde2" stroke-width="1.4"/>
      </svg>
      <span class="rule"></span>
      <span class="value">hello@fernguild</span>
    </div>

    <div class="contact-row row--social">
      <span class="social-dot"></span>
      <span class="rule"></span>
      <span class="value">@ferngild</span>
    </div>
  </section>

  <section class="card card--back" aria-label="Card back">
    <div class="brand-name">Fern Guildworks</div>
    <div class="tagline">Mentoring | Teams | Learning</div>
    <div class="website">www.fernguildworks.com</div>
    <div class="back-handle">
      <span class="social-dot"></span>
      <span class="value">@ferngild</span>
    </div>
    <div class="stripes">
      <span class="stripe--white"></span>
      <span class="stripe--band"></span>
    </div>
  </section>
</body>
</html>
```